Business Card Design with new logo

Dorian Pelleway 4172
E 118th St Tallowford, IL 62488
Cell: 217-555-0193
pellewayrestoration@mailvane.test

Classic Car Restoration Services Buy Sell Trade Consign

Dorian Pelleway 9698
Cell: 217-555-0193

```html
<!DOCTYPE html>
<html lang="en">
<head>
<meta charset="utf-8">
<title>Pelleway Restoration LLC — Business Card</title>
<link rel="stylesheet" href="https://fonts.googleapis.com/css2?family=Roboto:wght@400;500;700&display=swap">
<style>
  :root {
    --backdrop: #6f4a33;
    --paper: #f3f3f3;
    --brand-red: #c4242a;
    --brand-red-light: #e0393a;
    --brand-red-dark: #b01f25;
    --navy: #13222f;
    --ink: #333;
    --rule: #333;
    --white: #ffffff;
  }
  * { margin: 0; padding: 0; box-sizing: border-box; }
  html, body { width: 1200px; height: 960px; overflow: hidden; }
  body {
    background: var(--backdrop);
    font-family: "Roboto", Arial, sans-serif;
    position: relative;
  }
  .card {
    position: absolute;
    width: 600px;
    height: 343px;
    box-shadow: 0 3px 8px rgba(0,0,0,.45);
  }
  .card-front { left: 314px; top: 113px; background: var(--paper); }
  .card-back {
    left: 311px; top: 472px;
    background: radial-gradient(ellipse at 50% 40%, var(--brand-red-light) 0%, var(--brand-red) 55%, var(--brand-red-dark) 100%);
  }
  .edge-red { position: absolute; left: 0; top: 0; width: 21px; height: 107px; background: var(--brand-red); }
  .edge-navy { position: absolute; left: 0; top: 113px; width: 21px; height: 230px; background: var(--navy); }

  .brand { position: absolute; left: 62px; top: 88px; }
  .brand-name {
    font-weight: 700; font-size: 27px; letter-spacing: 1px;
    color: var(--navy); line-height: 1;
  }
  .brand-sub {
    margin-top: 9px; font-weight: 700; font-size: 11px;
    letter-spacing: 4.6px; color: var(--brand-red);
  }

  .person { position: absolute; right: 35px; top: 202px; text-align: right; }
  .person-name { font-weight: 500; font-size: 21px; color: var(--brand-red); line-height: 1.1; }
  .person-role { font-weight: 500; font-size: 14px; color: var(--navy); margin-top: 3px; }

  .rule { position: absolute; left: 181px; right: 35px; top: 259px; border-top: 1px solid var(--rule); }

  .contacts { position: absolute; left: 62px; top: 250px; list-style: none; }
  .contacts li {
    display: flex; align-items: center; gap: 7px;
    font-size: 14px; color: var(--ink); height: 19.5px;
  }
  .contacts svg { width: 12px; height: 12px; flex: none; }

  .address {
    position: absolute; right: 35px; top: 270px; text-align: right;
    font-size: 14px; color: var(--ink); line-height: 19.5px;
  }

  .back-name {
    position: absolute; left: 0; right: 0; top: 110px; text-align: center;
    font-weight: 700; font-size: 56px; letter-spacing: 3px; color: var(--white);
  }
  .tagline {
    position: absolute; left: 0; right: 0; top: 290px; text-align: center;
    font-size: 14px; color: var(--white);
  }
</style>
</head>
<body>
  <section class="card card-front">
    <div class="edge-red"></div>
    <div class="edge-navy"></div>

    <div class="brand">
      <div class="brand-name">PELLEWAY</div>
      <div class="brand-sub">RESTORATION LLC</div>
    </div>

    <div class="person">
      <div class="person-name">JOHN SMITH</div>
      <div class="person-role">CEO/FOUNDER</div>
    </div>

    <div class="rule"></div>

    <ul class="contacts">
      <li>
        <svg viewBox="0 0 12 12" aria-hidden="true"><rect x="3" y="0.5" width="6" height="11" rx="1" fill="none" stroke="#c4242a" stroke-width="1.4"/><rect x="5" y="9" width="2" height="1" fill="#c4242a"/></svg>
        217-555-0193
      </li>
      <li>
        <svg viewBox="0 0 12 12" aria-hidden="true"><rect x="0.5" y="2.5" width="11" height="7" fill="#c4242a"/><path d="M0.5 2.5 L6 6.5 L11.5 2.5" fill="none" stroke="#f3f3f3" stroke-width="1"/></svg>
        pellewayrestoration@mailvane.test
      </li>
      <li>
        <svg viewBox="0 0 12 12" aria-hidden="true"><circle cx="6" cy="6" r="5.5" fill="#c4242a"/><path d="M3 4 Q5 3 6 5 T9 8" fill="none" stroke="#f3f3f3" stroke-width="1"/></svg>
        www.pellewayrestoration.test
      </li>
    </ul>

    <div class="address">Dorian Pelleway 4172<br>E 118th St Tallowford, IL 62488</div>
  </section>

  <section class="card card-back">
    <div class="back-name">PELLEWAY</div>
    <div class="tagline">Classic Car Restoration Services Buy Sell Trade Consign</div>
  </section>
</body>
</html>
```